Brindlecove.io - Please redesign to make it look better from current design

We already have the current website, that you can access but we think it can improve from current version.
Brindlecove is a cryptocurrency hedge fund that allow you to participate in the hedge fund with cryptocurrency such as eth.
At current phase, we are doing an ICO, then we want to make sure that the website it looks professional, beautiful and trustable enough for investors after looking at our website.
Target Market(s)
Investors
Industry/Entity Type
Investment
Coding
Coded - Design and coding required
Number of Pages Required
1 page
Look and feel

```html
<!DOCTYPE html>
<html lang="en">
<head>
<meta charset="utf-8">
<title>Brindlecove – Digital Asset Management</title>
<link href="https://fonts.googleapis.com/css2?family=Roboto+Condensed:wght@400;700&family=Open+Sans:wght@400;600;700&display=swap" rel="stylesheet">
<style>
:root{
  --blue:#1a8ccc;
  --blue-dark:#137ab5;
  --ink:#333333;
  --body:#555555;
  --white:#ffffff;
  --grey-band:#f1f1f1;
  --card-grey:#e3e3e3;
  --sky:#d4e8f4;
  --footer:#1c1c1c;
  --footer-text:#d8d8d8;
}
*{margin:0;padding:0;box-sizing:border-box}
html,body{width:1200px;height:3025px;overflow:hidden;background:var(--white)}
body{font-family:"Open Sans",Arial,sans-serif;color:var(--body);position:relative}
.abs{position:absolute}
.btn{position:absolute;background:var(--blue);color:var(--white);font-family:"Roboto Condensed","Arial Narrow",sans-serif;font-weight:700;font-size:15px;text-transform:uppercase;display:flex;align-items:center;justify-content:center;border-radius:3px;letter-spacing:.3px}

/* hero */
.hero{position:absolute;left:0;top:0;width:1200px;height:640px;overflow:hidden}
.hero-photo{position:absolute;inset:0;background:radial-gradient(ellipse at 50% 55%,#5a4a3e 0%,#3a322c 45%,#211d1a 100%)}
.hero-shade{position:absolute;inset:0;background:rgba(0,0,0,.35)}
.brand{position:absolute;display:flex;align-items:center;gap:12px;color:var(--white);font-family:"Open Sans",Arial,sans-serif;font-weight:600}
.brand .dot{width:26px;height:26px;border-radius:50%;background:var(--white)}
.nav{position:absolute;top:64px;right:106px;display:flex;gap:30px}
.nav a{color:var(--white);text-decoration:none;font-family:"Roboto Condensed","Arial Narrow",sans-serif;font-size:16px;text-transform:uppercase}
.hero-title{position:absolute;left:0;width:1200px;text-align:center;color:var(--white);font-family:"Roboto Condensed","Arial Narrow",sans-serif;font-weight:700}
.hero-copy{position:absolute;left:340px;width:520px;top:374px;text-align:center;color:#eee;font-size:12.5px;line-height:25px}
.hero-btn{left:538px;top:452px;width:124px;height:36px;border-radius:18px;border:2px solid var(--white);font-weight:400;font-size:13px;gap:8px}
.dots{position:absolute;top:555px;left:569px;display:flex;gap:6px}
.dots span{width:14px;height:14px;border-radius:50%;border:2px solid var(--white)}
.dots span.on{background:var(--white)}

/* welcome */
.section-title{position:absolute;left:0;width:1200px;text-align:center;font-family:"Roboto Condensed","Arial Narrow",sans-serif;font-weight:700;color:var(--ink)}
.section-title em{font-style:normal;color:var(--blue)}
.rule{position:absolute;left:575px;width:50px;height:3px;background:var(--blue)}
.welcome-copy{position:absolute;left:150px;width:900px;text-align:center;font-size:11.5px;line-height:23px}
.welcome-copy p+p{margin-top:12px}

/* definition */
.definition{position:absolute;left:0;top:1051px;width:1200px;height:476px;background:linear-gradient(135deg,#f6f6f6,#e9e9e9)}
.laptop-art{position:absolute;left:97px;top:1146px;width:472px;height:302px;background:linear-gradient(180deg,#6e6e6e 0%,#4a4a4a 70%,#c9c9c9 71%,#e1e1e1 100%);border-radius:8px}
.def-title{position:absolute;left:605px;top:1160px;font-family:"Roboto Condensed","Arial Narrow",sans-serif;font-weight:700;font-size:32px;color:var(--ink)}
.def-copy{position:absolute;left:605px;top:1216px;width:500px;font-size:11.5px;line-height:23px}
.def-copy p+p{margin-top:12px}

/* team */
.team-title{position:absolute;left:0;width:1200px;top:1610px;text-align:center;font-family:"Roboto Condensed","Arial Narrow",sans-serif;font-weight:400;font-size:32px;color:var(--ink)}
.quote-card{position:absolute;background:var(--card-grey);border-radius:8px;padding:24px 18px 0 64px;font-size:11px;line-height:21.5px;color:var(--body)}
.quote-card::after{content:"";position:absolute;left:50%;bottom:-12px;margin-left:-12px;border-left:12px solid transparent;border-right:12px solid transparent;border-top:12px solid var(--card-grey)}
.quote-card .mark{position:absolute;left:18px;top:10px;font-family:Georgia,serif;font-size:52px;line-height:52px;color:#9a9a9a;font-weight:700}
.quote-card.featured{background:var(--blue);color:var(--white);font-weight:700;padding:28px 22px 0 70px}
.quote-card.featured::after{border-top-color:var(--blue)}
.quote-card.featured .mark{color:var(--white)}
.avatar{position:absolute;width:82px;height:82px;border-radius:50%;background:radial-gradient(circle at 50% 40%,#a88270,#4c3a32)}
.avatar.featured{border:3px solid var(--blue)}
.member{position:absolute;text-align:center;width:300px}
.member .name{font-size:17px;color:var(--ink)}
.member .role{font-size:12.5px;color:var(--body)}

/* process */
.process{position:absolute;left:0;top:2182px;width:1200px;height:474px;background:var(--sky)}
.process h2{position:absolute;left:99px;top:58px;font-family:"Roboto Condensed","Arial Narrow",sans-serif;font-size:34px;font-weight:700;color:var(--ink)}
.process h3{position:absolute;left:99px;font-family:"Roboto Condensed","Arial Narrow",sans-serif;font-weight:400;text-transform:uppercase;color:var(--ink)}
.process .model{position:absolute;left:99px;top:150px;width:530px;font-size:11px;line-height:21px}
.dist{position:absolute;left:99px;top:276px;list-style:none;font-size:11px}
.dist li{height:24.5px;display:flex;align-items:center;gap:14px}
.dist li::before{content:"";width:9px;height:9px;border-radius:50%;background:var(--ink);flex:none}
.process-art{position:absolute;left:655px;top:86px;width:485px;height:304px;background:linear-gradient(180deg,#e8f1f7,#c6dceb);border-radius:6px}

/* footer */
.footer{position:absolute;left:0;top:2656px;width:1200px;height:369px;background:var(--footer);color:var(--footer-text)}
.footer h4{position:absolute;font-family:"Roboto Condensed","Arial Narrow",sans-serif;font-weight:400;font-size:17px;text-transform:uppercase;color:var(--white)}
.footer .line{position:absolute;display:flex;align-items:flex-start;gap:18px;font-size:13px;line-height:19px}
.footer .line svg{flex:none;margin-top:2px}
.socials{position:absolute;left:97px;top:184px;display:flex;gap:4px}
.socials span{width:26px;height:26px;border-radius:50%;border:2px solid var(--white)}
.signup-copy{position:absolute;left:665px;top:96px;width:280px;font-size:11px;line-height:19px;white-space:nowrap}
.field{position:absolute;left:665px;top:146px;width:248px;height:40px;background:var(--white);color:#777;font-size:11.5px;padding-left:14px;display:flex;align-items:center}
.sub-btn{left:665px;top:202px;width:100px;height:40px;font-family:"Open Sans",Arial,sans-serif;font-weight:600;font-size:11.5px;border-radius:0}
.quick{position:absolute;left:1012px;top:96px;list-style:none;font-size:12.5px;line-height:24px}
.copyright{position:absolute;left:0;width:1200px;top:318px;text-align:center;font-size:12.5px}
</style>
</head>
<body>

<header class="hero">
  <div class="hero-photo" role="img" aria-label="Photo of a wooden desk with laptop, tablet, notebook, camera and coffee seen from above"></div>
  <div class="hero-shade"></div>
  <div class="brand" style="left:97px;top:60px;font-size:22px"><span class="dot"></span>brindlecove</div>
  <nav class="nav">
    <a href="#">Home</a><a href="#">About us</a><a href="#">Our services</a><a href="#">Blog</a><a href="#">Contact us</a>
  </nav>
  <h1 class="hero-title" style="top:256px;font-size:58px;line-height:64px">BRINDLECOVE</h1>
  <h2 class="hero-title" style="top:320px;font-size:36px;line-height:44px">DIGITAL ASSET MANAGEMENT</h2>
  <p class="hero-copy">Brindlecove enable companies and investors to facilities business operation in modern digital world, including asset management on hedge fund strategy model</p>
  <span class="btn hero-btn">Read more
    <svg width="14" height="14" viewBox="0 0 14 14"><circle cx="7" cy="7" r="7" fill="#fff"/><path d="M6 4l3 3-3 3" stroke="#1a8ccc" stroke-width="2" fill="none"/></svg>
  </span>
  <div class="dots"><span class="on"></span><span></span><span></span></div>
</header>
<svg class="abs" style="left:0;top:560px" width="1200" height="90" viewBox="0 0 1200 90">
  <polygon points="0,8 600,74 1200,8 1200,90 0,90" fill="#fff"/>
  <polyline points="0,8 600,74 1200,8" fill="none" stroke="#1a8ccc" stroke-width="5"/>
</svg>

<section>
  <h2 class="section-title" style="top:718px;font-size:40px">WELCOME TO <em>BRINDLECOVE</em></h2>
  <div class="rule" style="top:780px"></div>
  <div class="welcome-copy" style="top:806px">
    <p>Sed ut perspiciatis unde omnis iste natus error sit voluptatem accusantium doloremque laudantium, totam rem aperiam, eaque ipsa quae ab illo inventore veritatis et quasi archcto beatae vitae dicta sunt explicabo. Nemo enim ipsam voluptatem quia voluptas sit aspernatur aut odit aut fugit, sed quia consequuntur magni dolores eos qui ratione voluptatem sequi nesciunt. Neque porro quisquam est, qui dolorem ipsum quia dolor sit amet, consectetur, adipisci velit, sed quia</p>
    <p>Sed ut perspiciatis unde omnis iste natus error sit voluptatem accusantium doloremque laudantium, totam rem aperiam, eaque ipsa quae ab illo inventore veritatis et quasi archcto beatae vitae dicta sunt explicabo. Nemo enim ipsam voluptatem quia voluptas sit aspernatur aut odit aut fugit, sed quia consequuntur</p>
  </div>
  <span class="btn" style="left:545px;top:955px;width:111px;height:34px">Read more</span>
</section>

<section class="definition"></section>
<div class="laptop-art" role="img" aria-label="Illustration of an open laptop showing a cryptocurrency coin over binary digits"></div>
<h2 class="def-title">DEFINITION</h2>
<div class="def-copy">
  <p>Brindlecove process and manages on hedge fund strategy models which invests in a diversified portfolio of blockchain tokens. Blockchain tokens are emerging which add a monetary incentive layer to p2p protocols and facilitate equity crowdfunding that anyone in the world can participate in.</p>
  <p>This means open source software developers can monetize their networks at the protocol level and users of the network are the equity owners of the network. For this conditions, returns will go to holders of the tokens.</p>
</div>
<span class="btn" style="left:605px;top:1398px;width:111px;height:34px">Read more</span>

<section>
  <h2 class="team-title">EXECUTIVE TEAM</h2>

  <div class="quote-card" style="left:107px;top:1714px;width:276px;height:212px"><span class="mark">&ldquo;</span>As a hedge fund manager, Kittipat Worawong is the Chief Executive Officer of Harrowgate Capital LLC, an investment manager of Ironvale Metal Fund SP (Long-Short Equity Fund, investing in U.S. Stock Market) and Kestrel Peak Fund (Managed Futures Fund.</div>
  <div class="quote-card featured" style="left:434px;top:1696px;width:322px;height:246px"><span class="mark">&ldquo;</span>Nattapong has various experienced on cryptocurrency and blockchain technology. He created what was the world's 4th most valuable cryptocurrency in February 2014. He is also the world's first person to implement stealth addresses in QX-Wallets, improving cryptocurrency anonymity.</div>
  <div class="quote-card" style="left:811px;top:1714px;width:276px;height:212px"><span class="mark">&ldquo;</span>Chanin Rattanapong embeds a decade of experience in brand building, strategic planning, and marketing communication across the global agencies, such as Northfield Group, Bramwell, Lantern Partners, Sorahide. His seasoned specialty</div>

  <div class="avatar" role="img" aria-label="Portrait photo of the director" style="left:200px;top:1946px"></div>
  <div class="avatar featured" role="img" aria-label="Portrait photo of the technical advisor" style="left:551px;top:1966px"></div>
  <div class="avatar" role="img" aria-label="Portrait photo of the marketing consultant" style="left:906px;top:1946px"></div>

  <div class="member" style="left:91px;top:2040px"><div class="name">Kittipat Worawong</div><div class="role">Director</div></div>
  <div class="member" style="left:445px;top:2058px"><div class="name">Nattapong Sirikul</div><div class="role">Technical advisor</div></div>
  <div class="member" style="left:797px;top:2032px"><div class="name">Chanin Rattanapong</div><div class="role">Marketing Consultant</div></div>
</section>

<section class="process">
  <h2>PROCESS</h2>
  <h3 style="top:118px;font-size:19px">Hedge fund model</h3>
  <p class="model">Brindlecove run on closed-end fund (CEF) model which offers its shares to investors and utilize the fund to speculate and invest in the innovative blockchain tokens. Brindlecove will charge an upfront annual operation fee 4% of the money raised during the ICO. After that, the fund will charge a quarterly performance of 50% on the net profit made.</p>
  <h3 style="top:246px;font-size:15px">Net profit distribution</h3>
  <ul class="dist">
    <li>50 % of net profit is distributed to investors</li>
    <li>0 – 5 % net profit &gt; 0% performance fee</li>
    <li>5 – 10% net profit &gt; 5% performance fee</li>
    <li>10-15 % net profit &gt; 13% performance fee</li>
    <li>&gt; 15% net profit &gt; 15% performance fee</li>
    <li>The remainder (50% minus performance fee, so at least 35%) is reinvested</li>
  </ul>
  <div class="process-art" role="img" aria-label="Line illustration of a laptop with coins, cloud, database and network icons around it"></div>
</section>

<footer class="footer">
  <div class="brand" style="left:97px;top:88px;font-size:20px"><span class="dot"></span>brindlecove</div>
  <div class="socials" aria-label="Social links"><span></span><span></span><span></span><span></span></div>

  <h4 style="left:343px;top:62px">Contact us</h4>
  <div class="line" style="left:343px;top:106px">
    <svg width="16" height="20" viewBox="0 0 16 20"><path d="M8 1a6 6 0 0 1 6 6c0 5-6 12-6 12S2 12 2 7a6 6 0 0 1 6-6z" fill="none" stroke="#d8d8d8" stroke-width="1.6"/><circle cx="8" cy="7" r="2" fill="#d8d8d8"/></svg>
    <span>Brindlecove<br>4821 LM, Hollerdam Netherlands.</span>
  </div>
  <div class="line" style="left:343px;top:158px">
    <svg width="16" height="16" viewBox="0 0 16 16"><path d="M3 1l3 3-2 2c1 2 3 4 5 5l2-2 3 3-2 3C7 15 1 9 1 3z" fill="none" stroke="#d8d8d8" stroke-width="1.4"/></svg>
    <span>Phone : 555 0142 7700</span>
  </div>
  <div class="line" style="left:343px;top:190px">
    <svg width="18" height="14" viewBox="0 0 18 14"><rect x="1" y="1" width="16" height="12" fill="none" stroke="#d8d8d8" stroke-width="1.4"/><path d="M1 1l8 7 8-7" fill="none" stroke="#d8d8d8" stroke-width="1.4"/></svg>
    <span>info@brindlecove.io</span>
  </div>

  <h4 style="left:665px;top:62px">Sign up to receive email</h4>
  <p class="signup-copy">Excepteur sint occaecat cupidatat non<br>proident, sunt in culpa qui Nemo enim ipsam</p>
  <div class="field">Enter Name</div>
  <span class="btn sub-btn">SUBSCRIBE</span>

  <h4 style="left:1012px;top:62px">Quick links</h4>
  <ul class="quick">
    <li>Home</li><li>Who we are</li><li>What we do</li><li>What we think</li><li>Blog</li><li>Contact us</li>
  </ul>

  <p class="copyright">Copyright © Brindlecove 2017. All rights reserved.</p>
</footer>

</body>
</html>
```